Modern business card design for professional copywriter

I'd like a business card design that I can use to have my cards printed out by plink.com as a squared corners business card (see artwork and design guidelines here: https://help.plink.com/hc/en-gb/sections/300481726-PLINK-Product-Templates)

The design should be clean and modern and reflect the colours, tone and branding on my website: https://noravestrel.com.au

Target Market(s)

Professionals, B2B small business owners

Industry/Entity Type

Business

Contact Information for Business Card

Nora Vestrel
m: 0427 593 864
e: nora@noravestrel.com.au
w: noravestrel.com.au

Font styles to use
Sans Serif

Requirements
Must have
• Tagline: "Smart copywriting for clever business people"
• Brand colours: fd8000, 009984, 666666 and black
Nice to have

```html
<!DOCTYPE html>
<html lang="en">
<head>
<meta charset="utf-8">
<title>Nora Vestrel – Business Card</title>
<link rel="stylesheet" href="https://fonts.googleapis.com/css2?family=Source+Sans+3:wght@300;400;600&display=swap">
<style>
  :root {
    --stage: #6b6b6b;
    --stage-light: #787878;
    --card-front: #f2f2f2;
    --teal: #159a84;
    --teal-light: #1fa891;
    --orange: #fd8000;
    --ink: #111111;
    --white: #ffffff;
  }
  * { margin: 0; padding: 0; box-sizing: border-box; }
  html, body {
    width: 1200px; height: 900px; overflow: hidden;
  }
  body {
    position: relative;
    background: radial-gradient(ellipse at 50% 30%, var(--stage-light) 0%, var(--stage) 60%);
    font-family: "Source Sans 3", "Helvetica Neue", Arial, sans-serif;
  }
  .card {
    position: absolute;
    top: 170px;
    width: 347px;
    height: 561px;
  }
  .card-front { left: 259px; background: var(--card-front); }
  .card-back {
    left: 631px;
    background: var(--teal);
    overflow: hidden;
  }
  .brand-mark {
    position: absolute;
    top: 312px; left: 0; width: 100%;
    display: flex; justify-content: center; align-items: center; gap: 10px;
  }
  .brand-dot {
    width: 14px; height: 14px; border-radius: 50%;
    background: var(--orange);
  }
  .brand-name {
    font-size: 40px; font-weight: 400; color: var(--teal);
    letter-spacing: -0.5px; line-height: 1;
  }
  .person-name {
    position: absolute; top: 345px; left: 0; width: 100%;
    text-align: center;
    font-size: 25px; font-weight: 600; letter-spacing: 0.5px;
    color: var(--teal);
  }
  .person-name .surname { color: var(--orange); }
  .divider {
    position: absolute; top: 399px; left: 100px;
    width: 147px; height: 3px;
    background: linear-gradient(90deg, rgba(253,128,0,0.35), var(--orange) 20%, var(--orange) 80%, rgba(253,128,0,0.35));
    border-radius: 2px;
  }
  .contact-icons {
    position: absolute; top: 431px; left: 0; width: 100%;
    display: flex; justify-content: center; gap: 7px;
  }
  .contact-icons svg { width: 13px; height: 13px; fill: var(--teal); }
  .contact-list {
    position: absolute; top: 456px; left: 0; width: 100%;
    list-style: none; text-align: center;
    font-size: 15.5px; line-height: 20px; color: var(--ink);
  }
  .back-glow {
    position: absolute; inset: 0;
    background:
      linear-gradient(155deg, rgba(255,255,255,0) 35%, rgba(255,255,255,0.05) 50%, rgba(255,255,255,0) 70%),
      radial-gradient(ellipse at 100% 10%, var(--teal-light) 0%, rgba(31,168,145,0) 55%);
  }
  .tagline {
    position: absolute; inset: 0;
    color: var(--white); font-weight: 400; text-transform: uppercase;
  }
  .tagline span {
    position: absolute; left: 0; width: 100%;
    text-align: center; line-height: 1; white-space: nowrap;
  }
  .t-smart { top: 96px; font-size: 80px; letter-spacing: 3px; }
  .t-copy { top: 196px; font-size: 38px; letter-spacing: 1.5px; }
  .t-clever { top: 260px; font-size: 38px; letter-spacing: 2px; }
  .t-business { top: 318px; font-size: 50px; letter-spacing: 2px; }
  .t-people { top: 393px; font-size: 70px; letter-spacing: 2px; }
</style>
</head>
<body>
  <section class="card card-front">
    <div class="brand-mark">
      <span class="brand-dot"></span>
      <span class="brand-name">Nora Vestrel</span>
    </div>
    <h1 class="person-name">NORA <span class="surname">VESTREL</span></h1>
    <div class="divider"></div>
    <div class="contact-icons">
      <svg viewBox="0 0 16 16" aria-label="Mobile"><path d="M4 0h8a1 1 0 0 1 1 1v14a1 1 0 0 1-1 1H4a1 1 0 0 1-1-1V1a1 1 0 0 1 1-1zm1 2v10h6V2zm3 11a1 1 0 1 0 0 2 1 1 0 0 0 0-2z"/></svg>
      <svg viewBox="0 0 16 16" aria-label="Email"><path d="M0 3h16v10H0zm1.5 1.2v.3L8 9l6.5-4.5v-.3zM1 6v6h14V6L8 10.5z"/></svg>
      <svg viewBox="0 0 16 16" aria-label="Website"><path d="M8 0a8 8 0 1 0 0 16A8 8 0 0 0 8 0zm-1 2.2C5.5 3 5 4 4.5 5H3a6 6 0 0 1 4-2.8zM2.4 7h3.2c-.1.7-.1 1.3 0 2H2.4a6 6 0 0 1 0-2zm8 0h3.2a6 6 0 0 1 0 2h-3.2c.1-.7.1-1.3 0-2zM9 2.2A6 6 0 0 1 13 5h-1.5C11 4 10.5 3 9 2.2zM7.6 7h.8v2h-.8zM3 11h1.5c.5 1 1 2 2.5 2.8A6 6 0 0 1 3 11zm8.5 0H13a6 6 0 0 1-4 2.8c1.5-.8 2-1.8 2.5-2.8z"/></svg>
    </div>
    <ul class="contact-list">
      <li>0427 593 864</li>
      <li>nora@noravestrel.com.au</li>
      <li>noravestrel.com.au</li>
    </ul>
  </section>

  <section class="card card-back">
    <div class="back-glow" role="img" aria-label="Soft teal light sweep decoration"></div>
    <h2 class="tagline">
      <span class="t-smart">Smart</span>
      <span class="t-copy">Copywriting</span>
      <span class="t-clever">For Clever</span>
      <span class="t-business">Business</span>
      <span class="t-people">People</span>
    </h2>
  </section>
</body>
</html>
```